New Webpage for High Class Expert Witness Services Company

We are looking for a minimalist design for a webpage that just has our logo and an entry form offer to connect with one of our Liaisons.
The entry form should just ask for Name, Email, Contact Info and Description of Project.

Company Name is: The Marlow Crest Advisory Services

Number of Pages Required

1 page

```html
<!DOCTYPE html>
<html lang="en">
<head>
<meta charset="UTF-8">
<title>The Marlow Crest Advisory Services — Inquiry</title>
<link rel="stylesheet" href="https://fonts.googleapis.com/css2?family=Playfair+Display:wght@700&family=Cinzel:wght@400&family=Jost:wght@300;400&display=swap">
<style>
  :root {
    --page-bg: #f2f2f2;
    --panel-bg: #e7e7e8;
    --field-bg: #ececec;
    --field-border: #d2d2d4;
    --ink: #111111;
    --ink-soft: #555555;
    --ink-faint: #8a8a8a;
    --accent: #6b5a33;
    --accent-text: #f3ede0;
  }
  * { box-sizing: border-box; margin: 0; padding: 0; }
  html, body { width: 1200px; height: 840px; overflow: hidden; }
  body {
    background: var(--page-bg);
    color: var(--ink);
    font-family: "Jost", sans-serif;
    position: relative;
  }
  .brand {
    position: absolute; left: 28px; top: 42px;
    display: flex; align-items: center; gap: 12px;
  }
  .brand-mark { width: 22px; height: 22px; background: var(--ink); }
  .brand-name {
    font-family: "Cinzel", serif; font-weight: 400;
    font-size: 20px; letter-spacing: 0.04em; color: var(--ink);
  }
  .hero { position: absolute; left: 28px; top: 214px; width: 560px; }
  .hero-eyebrow { font-size: 14px; font-weight: 300; color: var(--ink-soft); margin-bottom: 22px; }
  .hero-title {
    font-family: "Playfair Display", serif; font-weight: 700;
    font-size: 66px; line-height: 1.14; letter-spacing: -0.005em;
  }
  .hero-tagline { margin-top: 16px; font-size: 15px; font-weight: 300; color: var(--ink-soft); }
  .page-footer {
    position: absolute; left: 28px; bottom: 22px;
    font-size: 10px; font-weight: 300; letter-spacing: 0.08em;
    text-transform: uppercase; color: var(--ink-faint);
  }
  .inquiry {
    position: absolute; left: 722px; right: 22px; top: 132px; bottom: 0;
    background: var(--panel-bg);
    padding: 28px 40px 0;
  }
  .inquiry-title { font-family: "Cinzel", serif; font-size: 23px; letter-spacing: 0.05em; }
  .inquiry-subtitle { font-size: 12px; font-weight: 300; color: var(--ink-soft); margin-top: 2px; }
  .inquiry-form { margin-top: 26px; }
  .field { margin-bottom: 20px; }
  .field-label { display: block; font-size: 11px; font-weight: 300; color: var(--ink-soft); margin-bottom: 6px; }
  .field-input {
    display: block; width: 100%; height: 38px;
    background: var(--field-bg); border: 1px solid var(--field-border);
    font: inherit;
  }
  .field-textarea { height: 98px; resize: none; }
  .submit-button {
    display: block; width: 100%; height: 48px; margin-top: 12px;
    background: var(--accent); color: var(--accent-text); border: none;
    font-family: "Jost", sans-serif; font-size: 13px; letter-spacing: 0.04em;
  }
  .privilege-note { text-align: center; font-size: 11px; font-weight: 300; color: var(--ink-soft); margin-top: 14px; }
  .panel-links {
    position: absolute; left: 0; right: 0; bottom: 22px;
    text-align: center; font-size: 10px; font-weight: 300;
    letter-spacing: 0.08em; text-transform: uppercase; color: var(--ink-faint);
  }
  .panel-links span { margin: 0 10px; }
</style>
</head>
<body>
  <header class="brand">
    <span class="brand-mark"></span>
    <span class="brand-name">The Marlow Crest Advisory Services</span>
  </header>

  <main class="hero">
    <p class="hero-eyebrow">Institutional Defense</p>
    <h1 class="hero-title">The Final<br>Word in Legal<br>Defense.</h1>
    <p class="hero-tagline">Discreet. Intelligent. Authoritative.</p>
  </main>

  <footer class="page-footer">© 2025 The Marlow Crest Advisory Services. All rights reserved.</footer>

  <aside class="inquiry">
    <h2 class="inquiry-title">Inquiry Protocol</h2>
    <p class="inquiry-subtitle">Secure Consultation Request</p>
    <form class="inquiry-form">
      <div class="field">
        <label class="field-label" for="full-name">Full Name</label>
        <input class="field-input" id="full-name" type="text">
      </div>
      <div class="field">
        <label class="field-label" for="email">Email</label>
        <input class="field-input" id="email" type="email">
      </div>
      <div class="field">
        <label class="field-label" for="contact">Contact Number</label>
        <input class="field-input" id="contact" type="tel">
      </div>
      <div class="field">
        <label class="field-label" for="project">Description of Project</label>
        <textarea class="field-input field-textarea" id="project"></textarea>
      </div>
      <button class="submit-button" type="button">REQUEST CONSULTATION</button>
      <p class="privilege-note">This communication is protected by privilege.</p>
    </form>
    <nav class="panel-links">
      <span>Legal Information</span><span>Privacy Policy</span><span>Security Protocol</span>
    </nav>
  </aside>
</body>
</html>
```